Jest Ventures Website - Corporate Comedy Show

I've created a company called "Jest Ventures". We put on corporate comedy shows for companies all over the country. I'd like to design a nice, sleek, professional website, similar to Rydex's: https://www.rydex-example.com. We like the one page layout.
Tagline: Your Team's Desk-Grin Ratio
I need the following sections:
1. first section would be scrolling images of the company logo and tagline, with 2 or 3 other scrolling images. Testimonials.
2. The next section below would be an about the company section. a small paragraph describing what we do.
4. The next section below would be for a promo video
5. The next section below would be for bios...my partner and I would have transparent head shots, side by side split-screen. When you hover over our headshots, a button for "bio" appears. When you click the "bio" button, an expanded bio appears.
6. Contact section. Newsletter subscription. A section where people enter their email and short message of what they're linking for that will link directly to our email addresses.
7. Additional content. Scrolling video gallery of our sketch videos. (a section that links to a page with videos and content)
Target Market(s)
Corporate Executives, Event Planners, Event Coordinators, Marketing and HR managers, Venue owners
Industry/Entity Type
It Company
Coding
Coded - Design and coding required
Number of Pages Required
1 page
Font styles to use
Other font styles liked:
- FunctionPro
Requirements
Must have
- -Please use the branded colors from the logo. Burgundy and Blue;
- -A contact section where people put in their email address, company they are from and a small memo to describe the event they're hosting, which will then get sent directly to our email accounts;
- -email accounts that are "marcus@thejestventures.com" and "dennis@thejestventures.com" that link to our gmail accounts
- -getting our domain linked and hosted and all setup (www.thejestventures.com- bought from DomainNook)
Nice to have
- Build in Wix because we are familiar with it and know how to update
Should not have
- basic, generic look. too much white space (but soon is good!)

```html
<!DOCTYPE html>
<html lang="en">
<head>
<meta charset="utf-8">
<title>Jest Ventures — Corporate Comedy Shows</title>
<link href="https://fonts.googleapis.com/css2?family=Open+Sans:ital,wght@0,300;0,400;0,600;0,700;1,400&display=swap" rel="stylesheet">
<style>
:root{
  --red:#d8383a;
  --blue:#2b86c5;
  --blue-light:#3b95d3;
  --dark:#2b2b2b;
  --darker:#222222;
  --ink:#333333;
  --muted:#8a8a8a;
  --grey-bg:#f1f1f1;
  --line:#e2e2e2;
  --white:#ffffff;
}
*{margin:0;padding:0;box-sizing:border-box}
html,body{width:1200px;height:3388px;overflow:hidden}
body{font-family:"Open Sans",Arial,sans-serif;color:var(--ink);background:var(--white);position:relative}
section,header,footer,div{position:relative}
a{color:inherit;text-decoration:none}
ul{list-style:none}

/* top bar */
.topbar{height:36px;background:var(--dark);display:flex;align-items:center;justify-content:space-between;padding:0 24px}
.topbar .social{display:flex;gap:10px}
.topbar .social span{width:14px;height:14px;background:#7b7b7b;border-radius:2px;display:block}
.topbar .actions{display:flex;gap:26px;font-size:13px;font-weight:600;text-transform:uppercase}
.topbar .callback{color:var(--blue-light)}
.topbar .signin{color:#cfcfcf;text-transform:none;font-weight:400}

/* nav */
.mainnav{height:124px;display:flex;align-items:center;justify-content:space-between;padding:0 28px 0 24px;border-bottom:1px solid var(--line)}
.brand{display:flex;align-items:center;gap:12px}
.brand .dot{width:54px;height:54px;border-radius:50%;background:var(--red)}
.brand .name{font-size:26px;font-weight:700;color:var(--dark);text-transform:uppercase;letter-spacing:-.5px}
.menu{display:flex;align-items:center}
.menu a{font-size:17px;color:#555;padding:8px 22px;border-left:1px solid var(--line)}
.menu a:first-child{border-left:0}
.menu a.active{color:var(--red);border-bottom:3px solid var(--red)}

/* hero */
.hero{height:540px;background:linear-gradient(180deg,#3a2a24 0%,#6b4a3a 35%,#4a3430 70%,#1e1a1a 100%)}
.hero .overlay{position:absolute;inset:0;background:rgba(0,0,0,.25)}
.hero h1{position:absolute;top:205px;width:100%;text-align:center;color:var(--white);font-size:42px;font-weight:400}
.hero .tagline{position:absolute;top:268px;width:100%;text-align:center;color:#f0e6e0;font-size:19px;font-weight:300}
.hero .play{position:absolute;top:318px;left:568px}

/* testimonials */
.testimonials{height:560px}
.section-title{text-align:center;font-size:28px;font-weight:600;color:var(--dark)}
.testimonials .section-title{padding-top:70px}
.quotes{display:grid;grid-template-columns:440px 440px;column-gap:70px;row-gap:60px;margin:50px 0 0 140px}
.quote{display:flex;gap:22px}
.avatar{flex:0 0 74px;height:92px;border-radius:46px;background:linear-gradient(180deg,#c9a68c,#7a5a48)}
.quote h3{font-size:15px;font-weight:700;text-transform:uppercase;color:var(--dark);margin:4px 0 10px}
.quote h3 span{color:var(--red);font-weight:400}
.quote p{font-size:14px;line-height:22px;color:var(--muted)}

/* what we do */
.whatwedo{height:290px;background:var(--grey-bg);text-align:center}
.whatwedo .section-title{padding-top:32px}
.whatwedo .intro{width:820px;margin:22px auto 0;font-size:14px;line-height:21px;color:#666}
.services{display:flex;justify-content:center;gap:100px;margin-top:36px}
.service{display:flex;flex-direction:column;align-items:center;gap:10px;font-size:14px;font-weight:700;color:var(--dark);text-transform:uppercase}

/* video */
.promo{height:440px;background:linear-gradient(135deg,#6b3b3a 0%,#9a6b5a 40%,#5b4d60 70%,#3c2f3a 100%)}
.promo .player{position:absolute;left:328px;top:100px;width:544px;height:308px;background:var(--white);box-shadow:0 6px 24px rgba(0,0,0,.4)}
.player .frame{position:absolute;left:0;top:0;width:544px;height:272px;background:linear-gradient(180deg,#f4f4f4,#dcdcdc)}
.player .controls{position:absolute;left:0;bottom:0;width:544px;height:36px;background:#2e2e2e;display:flex;align-items:center;gap:14px;padding:0 14px}
.controls .bar{flex:1;height:4px;background:#555;border-radius:2px;position:relative}
.controls .bar i{position:absolute;left:0;top:0;height:4px;width:28%;background:var(--white);border-radius:2px}

/* team */
.team{height:510px;display:flex}
.bios{width:588px;display:flex}
.bio{width:294px;height:510px;background:var(--blue);color:var(--white);text-align:center;padding-top:88px}
.bio.alt{background:var(--blue-light)}
.headshot{width:112px;height:112px;margin:0 auto;background:linear-gradient(180deg,#d9b79c,#8c6550);border:4px solid rgba(255,255,255,.35)}
.bio h4{font-style:italic;font-weight:400;font-size:15px;margin:22px 0 10px}
.bio p{width:200px;margin:0 auto;font-size:14px;line-height:21px;color:#e6f1f9}
.bio .toggle{width:30px;height:30px;border-radius:50%;background:var(--white);margin:36px auto 0}
.feature{width:612px;height:510px;background:linear-gradient(160deg,#4a4a4a,#2c2c2c);color:var(--white);text-align:center;padding:120px 70px 0}
.feature h3{font-size:15px;font-weight:700;text-transform:uppercase;margin-bottom:16px}
.feature p{font-size:14px;line-height:22px;color:#dddddd}
.feature .pager{display:flex;justify-content:center;gap:8px;margin-top:26px}
.feature .pager span{width:18px;height:18px;border-radius:50%;background:#777}
.feature .pager span:first-child{background:#bbb}

/* gallery */
.gallery{height:400px;display:flex;padding:60px 0 0 100px}
.thumbs{display:grid;grid-template-columns:repeat(3,190px);grid-auto-rows:150px;gap:24px 22px}
.thumb{background:linear-gradient(135deg,#fafafa,#e4e4e4);border:1px solid #ddd}
.thumb.warm{background:linear-gradient(135deg,#fbf3ef,#f1d8d0)}
.categories{margin-left:70px;width:380px}
.categories h2{font-size:30px;font-weight:300;color:#444;margin-bottom:14px;white-space:nowrap}
.categories li{font-size:14px;color:#777;padding:14px 0 12px;border-bottom:1px solid var(--line)}

/* newsletter + contact */
.newsletter{height:300px;background:var(--darker);text-align:center;color:var(--white);padding-top:28px}
.newsletter h2{font-size:28px;font-weight:700;letter-spacing:1px}
.newsletter p{font-size:14px;color:#bbb;margin:4px 0 16px}
.row{display:flex;justify-content:center;gap:0}
.field{height:42px;background:var(--white);color:#999;font-size:14px;text-align:left;padding:11px 16px}
.btn{width:170px;height:42px;background:var(--blue);font-size:14px;font-weight:700;padding-top:11px;text-transform:uppercase;color:var(--white)}
.subscribe .field{width:500px}
.contact{margin-top:26px}
.contact h3{font-size:16px;font-weight:700;text-transform:uppercase;letter-spacing:1px;margin-bottom:10px}
.contact .row{gap:8px}
.contact .email{width:210px}
.contact .company{width:210px}
.contact .memo{width:320px}
.contact .note{font-size:13px;color:#999;margin:10px 0 0}

/* footer */
.footnav{height:52px;background:var(--blue);display:flex;justify-content:center;align-items:center}
.footnav a{color:var(--white);font-size:14px;padding:0 18px;border-left:1px solid rgba(255,255,255,.4)}
.footnav a:first-child{border-left:0}
.bottom{height:136px;background:#f6f6f6;display:flex;justify-content:space-between;align-items:flex-start;padding:18px 22px}
.bottom small{font-size:13px;color:#777}
.bottom .social{display:flex;gap:8px}
.bottom .social span{width:22px;height:22px;border-radius:50%;background:#9a9a9a;display:block}
</style>
</head>
<body>

<header class="topbar">
  <div class="social"><span></span><span></span><span></span><span></span></div>
  <div class="actions"><a class="callback" href="#">Request a call back</a><a class="signin" href="#">Sign In</a></div>
</header>

<nav class="mainnav">
  <div class="brand"><span class="dot"></span><span class="name">Jest Ventures</span></div>
  <div class="menu">
    <a class="active" href="#">Home</a>
    <a href="#">What we do</a>
    <a href="#">Team</a>
    <a href="#">Videos</a>
    <a href="#">Testimonials</a>
    <a href="#">Contact us</a>
  </div>
</nav>

<section class="hero" role="img" aria-label="Photo of a laughing audience at a live comedy show">
  <div class="overlay"></div>
  <h1>Welcome to Jest Ventures</h1>
  <p class="tagline">Your Team's Desk-Grin Ratio</p>
  <svg class="play" width="64" height="64" viewBox="0 0 64 64" aria-hidden="true">
    <circle cx="32" cy="32" r="30" fill="rgba(255,255,255,.85)"/>
    <path d="M26 19 L46 32 L26 45 Z" fill="#333"/>
  </svg>
</section>

<section class="testimonials">
  <h2 class="section-title">Our Clients Testimonails</h2>
  <div class="quotes">
    <div class="quote">
      <div class="avatar" role="img" aria-label="Client portrait"></div>
      <div><h3>Nora Pellham, <span>Business Owner</span></h3>
      <p>Our team laughed for a full hour. The show felt tailored to us, sharp and warm, and people still quote the best lines at every weekly meeting.</p></div>
    </div>
    <div class="quote">
      <div class="avatar" role="img" aria-label="Client portrait"></div>
      <div><h3>Owen Saldana, <span>Business Owner</span></h3>
      <p>Booking was easy and the comics read the room perfectly. Executives and interns laughed together, which we honestly did not think was possible here.</p></div>
    </div>
    <div class="quote">
      <div class="avatar" role="img" aria-label="Client portrait"></div>
      <div><h3>Nora Pellham, <span>Business Owner</span></h3>
      <p>A great break in a long conference day. Clean, clever material about office life that landed with every single person in the ballroom that night.</p></div>
    </div>
    <div class="quote">
      <div class="avatar" role="img" aria-label="Client portrait"></div>
      <div><h3>Owen Saldana, <span>Business Owner</span></h3>
      <p>They met with our planners first and built jokes around our own quirks. The crowd loved it and asked us to book them again next year.</p></div>
    </div>
  </div>
</section>

<section class="whatwedo">
  <h2 class="section-title">What we do</h2>
  <p class="intro">We bring live comedy to the workplace. Our comedians write fresh sets about your industry, your meetings and your inbox, then perform them at offices, retreats and conferences across the country. Shows run from twenty minutes to a full evening, always clean, always sharp and always built to get your people laughing together.</p>
  <div class="services">
    <div class="service">
      <svg width="30" height="30" viewBox="0 0 30 30" aria-hidden="true"><rect x="10" y="2" width="10" height="16" rx="5" fill="#333"/><path d="M6 14a9 9 0 0 0 18 0M15 23v5M10 28h10" stroke="#333" stroke-width="2" fill="none"/></svg>
      Stand-up comedy</div>
    <div class="service">
      <svg width="30" height="30" viewBox="0 0 30 30" aria-hidden="true"><circle cx="10" cy="9" r="4" fill="#333"/><circle cx="20" cy="9" r="4" fill="#333"/><path d="M2 26c0-6 4-9 8-9s8 3 8 9M12 26c0-6 4-9 8-9s8 3 8 9" fill="#333"/></svg>
      Corporate and private shows</div>
    <div class="service">
      <svg width="30" height="30" viewBox="0 0 30 30" aria-hidden="true"><rect x="3" y="4" width="24" height="16" fill="none" stroke="#333" stroke-width="2"/><path d="M15 20v8M9 28h12M8 15l5-5 4 3 5-5" stroke="#333" stroke-width="2" fill="none"/></svg>
      Comedy workshops</div>
    <div class="service">
      <svg width="30" height="30" viewBox="0 0 30 30" aria-hidden="true"><path d="M6 24l2-7L21 4l5 5L13 22z" fill="#333"/><path d="M4 28h22" stroke="#333" stroke-width="2"/></svg>
      Events writing</div>
  </div>
</section>

<section class="promo" role="img" aria-label="Blurred photo of a festival crowd behind the promo video">
  <div class="player">
    <div class="frame" role="img" aria-label="Promo video still of the comedy troupe performing"></div>
    <div class="controls">
      <svg width="14" height="16" viewBox="0 0 14 16" aria-hidden="true"><path d="M1 1l12 7-12 7z" fill="#fff"/></svg>
      <div class="bar"><i></i></div>
      <svg width="16" height="14" viewBox="0 0 16 14" aria-hidden="true"><path d="M1 5h4l4-4v12l-4-4H1z" fill="#fff"/></svg>
      <svg width="14" height="14" viewBox="0 0 14 14" aria-hidden="true"><path d="M1 5V1h4M9 1h4v4M13 9v4H9M5 13H1V9" stroke="#fff" stroke-width="2" fill="none"/></svg>
    </div>
  </div>
</section>

<section class="team">
  <div class="bios">
    <div class="bio">
      <div class="headshot" role="img" aria-label="Headshot of Marcus Lane"></div>
      <h4>Marcus Lane</h4>
      <p>Founder and headliner with ten years on stage at clubs and corporate events nationwide.</p>
      <div class="toggle"></div>
    </div>
    <div class="bio alt">
      <div class="headshot" role="img" aria-label="Headshot of Dennis Hale"></div>
      <h4>Dennis Hale</h4>
      <p>Writer and host who turns office life into sharp, clean sets for every crowd.</p>
    </div>
  </div>
  <div class="feature" role="img" aria-label="Dimmed photo of a comedy stage behind the service description">
    <h3>Stand-up comedy</h3>
    <p>Our stand-up sets are written for the room. We study your company, your culture and your inside jokes, then craft a clean and clever show that gets everyone laughing, from the front desk to the corner office. Every set is fresh and no two events are ever alike.</p>
    <div class="pager"><span></span><span></span><span></span></div>
  </div>
</section>

<section class="gallery">
  <div class="thumbs">
    <div class="thumb" role="img" aria-label="Sketch video thumbnail illustration"></div>
    <div class="thumb warm" role="img" aria-label="Sketch video thumbnail illustration"></div>
    <div class="thumb" role="img" aria-label="Sketch video thumbnail illustration"></div>
    <div class="thumb warm" role="img" aria-label="Sketch video thumbnail illustration"></div>
    <div class="thumb" role="img" aria-label="Sketch video thumbnail illustration"></div>
    <div class="thumb warm" role="img" aria-label="Sketch video thumbnail illustration"></div>
  </div>
  <div class="categories">
    <h2>Browse By Categories</h2>
    <ul>
      <li>Office life sketches</li>
      <li>Meeting room moments</li>
      <li>Team building bits</li>
      <li>Holiday party specials</li>
      <li>Behind the scenes</li>
    </ul>
  </div>
</section>

<section class="newsletter">
  <h2>EMAIL NEWSLETTERS</h2>
  <p>Subscribe to receive our new videos, ideas, and news in your inbox.</p>
  <div class="row subscribe"><div class="field">Enter Email address</div><div class="btn">Subscribe</div></div>
  <div class="contact">
    <h3>Book a show</h3>
    <div class="row">
      <div class="field email">Your email</div>
      <div class="field company">Company</div>
      <div class="field memo">Short memo about your event</div>
      <div class="btn">Send</div>
    </div>
    <p class="note">Sent to marcus@thejestventures.com and dennis@thejestventures.com</p>
  </div>
</section>

<footer>
  <nav class="footnav">
    <a href="#">Home</a><a href="#">What we do</a><a href="#">Team</a><a href="#">Videos</a><a href="#">Testimonials</a><a href="#">Contact us</a>
  </nav>
  <div class="bottom">
    <small>©All rights reserved 2015</small>
    <div class="social"><span></span><span></span><span></span><span></span><span></span><span></span></div>
  </div>
</footer>

</body>
</html>
```